Business Card Design

The Corvella Companion Animal Foundation is a not-for-profit organization that provides the best quality care and rehabilitation for pets in need. All our guests are treated with dignity and respect in a loving atmosphere. We offer the training and rehabilitation needed to make the transition to a forever home smooth and effective. As a no-kill facility, we do a behavioral analysis of each of our guests and put together a plan to make sure they are ready for a forever home. Corvella means a place of great beauty, luxury, and contentment.
We are looking for a professional looking card, rather than cutesy, that makes people take us seriously as we need to raise significant funds to support our efforts. Would like the name of company used in a way to be logo-ish, so be creative there.

Target Market(s)

A wealthy, animal loving market.

Industry/Entity Type

Training

Contact Information for Business Card

Corvella Companion Animal Foundation
M. Grant Pellow, CEO
P.O. Box 4518, Larkmere, VT 05019
www.corvellapetshelter.example
(555) 555-0187

```html
<!DOCTYPE html>
<html lang="en">
<head>
<meta charset="utf-8">
<title>Corvella Companion Animal Foundation – Business Card</title>
<link href="https://fonts.googleapis.com/css2?family=Courgette&family=Open+Sans:ital,wght@1,700&display=swap" rel="stylesheet">
<style>
  :root {
    --backdrop: #b9b9b9;
    --card-white: #ffffff;
    --brand-orange: #e85505;
    --ink: #1c1c1c;
    --card-edge: #d8d8d8;
  }
  html, body {
    margin: 0;
    width: 1200px;
    height: 861px;
    overflow: hidden;
    background: var(--backdrop);
  }
  .card-sheet {
    position: relative;
    width: 1200px;
    height: 861px;
  }
  .card {
    position: absolute;
    top: 280px;
    width: 530px;
    height: 299px;
    box-shadow: 0 0 0 1px var(--card-edge);
  }
  .card--front { left: 50px; }
  .card--back  { left: 620px; }
  .card-bg { fill: var(--card-white); }
  .accent { fill: var(--brand-orange); }
  .wordmark {
    font-family: "Courgette", cursive;
    fill: var(--ink);
  }
  .contact {
    font-family: "Open Sans", sans-serif;
    font-weight: 700;
    font-style: italic;
    font-size: 12.5px;
    fill: var(--card-white);
  }
  .contact-icon { fill: var(--card-white); }
</style>
</head>
<body>
<main class="card-sheet">

  <svg class="card card--front" viewBox="0 0 550 310" xmlns="http://www.w3.org/2000/svg">
    <rect class="card-bg" width="550" height="310"/>
    <polygon class="accent" points="0,0 82,0 0,82"/>
    <polygon class="accent" points="0,226 0,310 82,310"/>
    <path class="accent" d="M340,0 H550 V310 H380 L462,196 Q482,165 462,132 Z"/>
    <text class="wordmark" x="30" y="146" font-size="36">Corvella</text>
    <text class="wordmark" x="22" y="184" font-size="30">Companion Animal Foundation</text>
  </svg>

  <svg class="card card--back" viewBox="0 0 550 310" xmlns="http://www.w3.org/2000/svg">
    <rect class="card-bg" width="550" height="310"/>
    <path class="accent" d="M488,0 H512 L550,40 V262 L505,310 H305 L160,196 Q128,170 162,140 Z"/>
    <g transform="translate(44,304) rotate(-90)">
      <text class="wordmark" x="0" y="0" font-size="22">Corvella</text>
      <text class="wordmark" x="8" y="24" font-size="20">Companion Animal Foundation</text>
    </g>
    <g transform="translate(182,202) rotate(-21)">
      <text class="contact" x="0" y="0">M. Grant Pellow, CEO P.O. Box 4518, Larkmere, VT 05019</text>
      <circle class="contact-icon" cx="12" cy="17" r="5"/>
      <text class="contact" x="26" y="21">www.corvellapetshelter.example</text>
      <path class="contact-icon" d="M42,33 q-2,0 -2,3 q1,6 7,8 q3,0 3,-2 l-2,-2 q-1,1 -2,0 q-2,-1 -3,-3 q0,-1 1,-1 z"/>
      <text class="contact" x="54" y="44">(555) 555-0187</text>
    </g>
  </svg>

</main>
</body>
</html>
```